Gift Bag Design

We need a gift bag designed for our practice. We are a upscale optometry practice. The gift bags are given to our patients when they pick up their eyewear. We would like to see a gift bag designed with the use of dark grays and purples with a nice texture. We want simple, elegant, and upscale. We really like something with the texture of lamivo laminate ashen reed style number 4812-93. We also use pantone 2695U for our purple colors.
Target Market(s)
Middle aged women that are fashionable
Industry/Entity Type
Eyewear
Requirements
Must have
- We must have use of our logo, which we've attached. The name of the business must be "clear path" or "bright lens studio", whichever works better. The dimensions of the bag must be 20.5 cm high x 12.5 cm wide x 7.5 deep.
Nice to have
- Our phone number 555-217-6094 and our website www.BrightLensStudioXY.com
Should not have
- No red, yellow

```html
<!DOCTYPE html>
<html lang="en">
<head>
<meta charset="utf-8">
<title>Bright Lens Studio – Gift Bag Dieline</title>
<link rel="stylesheet" href="https://fonts.googleapis.com/css2?family=Arimo:wght@400;700&family=Archivo+Black&display=swap">
<style>
  :root {
    --paper: #ffffff;
    --ink: #1a1a1a;
    --grey-dark: #3d3d3d;
    --grey-mid: #6e6e6e;
    --grey-light: #9a9a9a;
    --purple-deep: #2f2777;
    --purple: #3e3592;
    --purple-glow: #8d82c4;
    --text-light: #ffffff;
    --name-grey: #cfcfcf;
  }
  html, body {
    margin: 0;
    padding: 0;
    overflow: hidden;
    background: var(--paper);
  }
  .sheet {
    position: relative;
    width: 1200px;
    height: 924px;
    background: var(--paper);
    overflow: hidden;
    font-family: "Arimo", Arial, sans-serif;
  }
  .artwork {
    position: absolute;
    inset: 0;
  }
  .text-block {
    position: absolute;
    color: var(--text-light);
    text-align: center;
    transform: translateX(-50%);
    white-space: nowrap;
  }
  .brand-name {
    font-weight: 700;
    font-size: 31px;
    letter-spacing: 0.5px;
    color: var(--name-grey);
    display: flex;
    align-items: center;
    gap: 10px;
  }
  .brand-dot {
    width: 16px;
    height: 16px;
    border-radius: 50%;
    background: var(--name-grey);
    flex: none;
  }
  .brand-name--small {
    font-size: 19px;
    color: var(--text-light);
  }
  .tagline {
    font-family: "Archivo Black", "Arial Black", sans-serif;
    font-size: 16px;
    line-height: 19px;
    letter-spacing: 1.6px;
  }
  .contact {
    font-weight: 700;
    font-size: 16px;
  }
  .side-note {
    font-size: 11.5px;
    line-height: 14px;
  }
</style>
</head>
<body>
<div class="sheet">
  <svg class="artwork" width="1200" height="924" viewBox="0 0 1200 924" xmlns="http://www.w3.org/2000/svg">
    <defs>
      <linearGradient id="grain-tone" x1="0" y1="0" x2="1" y2="0">
        <stop offset="0" stop-color="#555"/>
        <stop offset="0.25" stop-color="#7a7a7a"/>
        <stop offset="0.5" stop-color="#5e5e5e"/>
        <stop offset="0.75" stop-color="#777"/>
        <stop offset="1" stop-color="#575757"/>
      </linearGradient>
      <linearGradient id="beam" x1="0" y1="0" x2="1" y2="0">
        <stop offset="0" stop-color="#2c2474"/>
        <stop offset="0.35" stop-color="#4a3f9c"/>
        <stop offset="0.5" stop-color="#5c52a8"/>
        <stop offset="0.65" stop-color="#4a3f9c"/>
        <stop offset="1" stop-color="#2c2474"/>
      </linearGradient>
      <linearGradient id="beam-glow" x1="0" y1="0" x2="0" y2="1">
        <stop offset="0" stop-color="#c9c2ea" stop-opacity="0.75"/>
        <stop offset="0.25" stop-color="#8d82c4" stop-opacity="0.25"/>
        <stop offset="1" stop-color="#8d82c4" stop-opacity="0"/>
      </linearGradient>
    </defs>

    <!-- laminate texture field -->
    <rect class="laminate-texture" x="0" y="63" width="1123" height="800" fill="url(#grain-tone)"
          role="img" aria-label="Dark grey woven reed laminate texture"/>

    <!-- purple spotlight beams on the front panels -->
    <g class="spotlight">
      <polygon points="131,63 237,63 350,863 5,863" fill="url(#beam)"/>
      <polygon points="131,63 237,63 300,500 68,500" fill="url(#beam-glow)"/>
    </g>
    <g class="spotlight">
      <polygon points="692,63 796,63 910,863 564,863" fill="url(#beam)"/>
      <polygon points="692,63 796,63 860,500 628,500" fill="url(#beam-glow)"/>
    </g>

    <!-- trim and crop marks -->
    <g class="crop-marks" stroke="var(--ink)" stroke-width="0.8" fill="none">
      <line x1="558" y1="8" x2="558" y2="43"/>
      <line x1="910" y1="8" x2="910" y2="43"/>
      <line x1="1123" y1="8" x2="1123" y2="43"/>
      <line x1="558" y1="881" x2="558" y2="918"/>
      <line x1="910" y1="881" x2="910" y2="918"/>
      <line x1="1120" y1="881" x2="1120" y2="918"/>
      <line x1="508" y1="59" x2="542" y2="59" stroke="#999"/>
      <line x1="508" y1="865" x2="542" y2="865" stroke="#999"/>
      <line x1="1140" y1="61" x2="1172" y2="61"/>
      <line x1="1140" y1="166" x2="1172" y2="166"/>
      <line x1="1140" y1="724" x2="1172" y2="724"/>
      <line x1="1140" y1="864" x2="1172" y2="864"/>
    </g>
    <g class="registration-marks" stroke="var(--ink)" stroke-width="0.8" fill="none">
      <g transform="translate(736 14)">
        <circle r="5"/><line x1="-12" y1="0" x2="12" y2="0"/><line x1="0" y1="-12" x2="0" y2="12"/>
      </g>
      <g transform="translate(736 910)">
        <circle r="5"/><line x1="-12" y1="0" x2="12" y2="0"/><line x1="0" y1="-12" x2="0" y2="12"/>
      </g>
      <g transform="translate(1183 446)">
        <circle r="5"/><line x1="-12" y1="0" x2="12" y2="0"/><line x1="0" y1="-12" x2="0" y2="12"/>
      </g>
    </g>
  </svg>

  <!-- front panel one -->
  <div class="text-block brand-name" style="left:182px; top:262px;"><span class="brand-dot"></span>Bright Lens Studio</div>
  <div class="text-block tagline" style="left:182px; top:364px;">Where your vision<br>means the world</div>
  <div class="text-block contact" style="left:161px; top:545px;">Phone:555-217-6094</div>
  <div class="text-block contact" style="left:168px; top:592px;">Web:www.brightlens studio.com</div>

  <!-- side panel one -->
  <div class="text-block brand-name brand-name--small" style="left:455px; top:104px;">Bright Lens Studio</div>
  <div class="text-block side-note" style="left:455px; top:545px;">To Learn More<br>About Eye Care,<br>Please Visit Us Online At<br>www.BrightLensStudioXY.com</div>

  <!-- front panel two -->
  <div class="text-block brand-name" style="left:738px; top:260px;"><span class="brand-dot"></span>Bright Lens Studio</div>
  <div class="text-block tagline" style="left:741px; top:357px;">Where your vision<br>means the world</div>
  <div class="text-block contact" style="left:726px; top:545px;">Phone:555-217-6094</div>
  <div class="text-block contact" style="left:733px; top:592px;">Web:www.brightlens studio.com</div>

  <!-- side panel two -->
  <div class="text-block brand-name brand-name--small" style="left:1018px; top:96px;">Bright Lens Studio</div>
  <div class="text-block side-note" style="left:1018px; top:546px;">To Learn More<br>About Eye Care,<br>Please Visit Us Online At<br>www.BrightLensStudioXY.com</div>
</div>
</body>
</html>
```